Briefpapier, Visitenkarten, Bindemappe, Brieumschläge....
Zielgruppe
Steuerberatung vorwiegen für Unternehmer
Aufgabenstellung
Ein Logo ist bereits vorhanden (siehe Analgen) kann aber gerne auch bei einer guten Idee modernisiert werden. Ganz ein neues Logo möchte ich meinen Kunden jedoch ersparen, da ich es erst von zwei Jahren gewechselt habe. Grundfarbe grün wie Pantone 2293 C.
Als Anhaltspunkt was derzeit bei im Einsatz ist, habe ich die entsprechenden Dateien hochgeladen.

```html
<!DOCTYPE html>
<html lang="de">
<head>
<meta charset="utf-8">
<title>Mappe – Steuerberater Konrad Velten</title>
<link rel="stylesheet" href="https://fonts.googleapis.com/css2?family=Roboto:wght@300;400;700;900&display=swap">
<style>
  :root {
    --green: #8dc63f;
    --white: #ffffff;
    --ink: #111111;
    --rule: #c8c8c8;
    --spine: #e6e6e6;
    --photo-light: #fdfdfd;
    --photo-mid: #ececec;
  }
  * { margin: 0; padding: 0; box-sizing: border-box; }
  html, body { width: 1200px; height: 835px; overflow: hidden; background: var(--white); }
  body { font-family: "Roboto", Arial, sans-serif; position: relative; }

  .folder { position: absolute; left: 0; top: 0; width: 677px; height: 835px; background: var(--white); border-right: 2px solid #9a9a9a; }

  .headline {
    position: absolute; background: var(--green); color: var(--white);
    font-weight: 700; font-size: 28px; letter-spacing: 1.1px; line-height: 52px;
    padding: 0 13px; box-shadow: 4px 4px 5px rgba(0,0,0,0.35); white-space: nowrap;
  }
  .headline--one { left: 45px; top: 70px; width: 474px; }
  .headline--two { left: 181px; top: 139px; width: 382px; padding-left: 21px; }

  .photo {
    position: absolute; left: 0; top: 225px; width: 580px; height: 376px;
    background: radial-gradient(ellipse 210px 170px at 310px 190px, var(--photo-mid) 0%, #f4f4f4 60%, var(--photo-light) 100%);
  }

  .divider { position: absolute; left: 0; top: 603px; width: 677px; height: 3px; background: var(--rule); }

  .spine-strip { position: absolute; left: 590px; top: 0; width: 42px; height: 810px; background: var(--spine); }

  .side-contact {
    position: absolute; left: 646px; color: var(--green); font-size: 12.5px; line-height: 16px;
    transform-origin: left top; transform: rotate(-90deg); white-space: nowrap;
  }

  .side-brand {
    position: absolute; left: 670px; top: 646px; transform-origin: left top;
    transform: rotate(90deg); display: flex; align-items: center; gap: 6px; white-space: nowrap;
  }
  .side-brand__mark { width: 30px; height: 30px; background: var(--green); }
  .side-brand__name { font-size: 13px; line-height: 13px; color: var(--ink); font-weight: 400; }

  .brand { position: absolute; left: 45px; top: 643px; display: flex; align-items: center; }
  .brand__mark { width: 123px; height: 123px; background: var(--green); margin-right: 15px; }
  .brand__name { font-size: 50px; line-height: 60px; color: var(--ink); }
  .brand__name strong { font-weight: 700; display: block; }
  .brand__name span { font-weight: 300; display: block; }

  .footer-band {
    position: absolute; left: 0; top: 818px; width: 677px; height: 17px; background: var(--green);
    color: var(--white); font-size: 9.5px; font-weight: 700; display: flex; align-items: center;
    padding-left: 45px; gap: 17px; white-space: nowrap;
  }
</style>
</head>
<body>
  <section class="folder">
    <div class="headline headline--one">ERGEBNISORIENTIERT DENKEN,</div>
    <div class="headline headline--two">PERSÖNLICH HANDELN.</div>

    <div class="photo" role="img" aria-label="Foto: weißes Sparschwein aus Porzellan auf weißem Grund"></div>

    <div class="divider"></div>

    <div class="spine-strip" role="img" aria-label="Rücken der Mappe mit Perforation für die Bindung"></div>

    <div class="side-contact" style="top:205px;">Tel.: 01234 / 567 89 - 00</div>
    <div class="side-contact" style="top:400px;">post@kanzlei-velten.de</div>
    <div class="side-contact" style="top:592px;">www.kanzlei-velten.de</div>

    <div class="side-brand">
      <div class="side-brand__name"><strong>Steuerberater</strong><br>Konrad Velten</div>
      <div class="side-brand__mark"></div>
    </div>

    <div class="brand">
      <div class="brand__mark"></div>
      <div class="brand__name"><strong>Steuerberater</strong><span>Konrad Velten</span></div>
    </div>

    <div class="footer-band">
      <span>post@kanzlei-velten.de</span>
      <span>www.kanzlei-velten.de</span>
      <span>Tel.: 01234 / 567 89 - 00</span>
      <span>Lindenweg 12, 12345 Musterstadt</span>
    </div>
  </section>
</body>
</html>
```